Need a flyer to leave behind when visiting clients or at shows

Glossy colorful tri-fold flyer with the same information that is on my web site www.brevalinkpro.com. I am open to a little modern or creative take on the typical brochure. I created the web site so I can provide any raw files needed from it. I would also like the ability to edit this flyer in the future in Adobe Photoshop Elements

```html
<!DOCTYPE html>
<html lang="en">
<head>
<meta charset="utf-8">
<title>Brevalink Healthcare Solutions – Tri-fold Brochure</title>
<link href="https://fonts.googleapis.com/css2?family=Montserrat:wght@300;400;500;700&display=swap" rel="stylesheet">
<style>
  :root {
    --page-bg: #e6e9f1;
    --violet: #5a47a0;
    --indigo: #4b54a8;
    --blue: #3a6fb4;
    --cyan: #08b4d4;
    --cyan-soft: #1c9fcf;
    --ink-purple: #7a3fd0;
    --white: #ffffff;
    --photo-light: #eef1f4;
    --photo-mid: #c9cfd6;
  }
  * { box-sizing: border-box; margin: 0; padding: 0; }
  html, body { width: 1200px; height: 1200px; overflow: hidden; }
  body {
    background: var(--page-bg);
    font-family: "Montserrat", sans-serif;
    color: var(--white);
  }
  .brochure {
    position: absolute;
    left: 98px; top: 225px;
    width: 1004px; height: 750px;
    overflow: hidden;
    box-shadow: 0 18px 40px rgba(40, 50, 90, 0.25);
  }
  .brochure-art { position: absolute; inset: 0; }
  .profile-name {
    position: absolute; left: 30px; top: 334px;
    font-size: 14px; line-height: 17px; font-weight: 400;
  }
  .profile-bio {
    position: absolute; left: 33px; top: 391px; width: 300px;
    font-size: 12.4px; line-height: 16.1px; font-weight: 300;
  }
  .headline {
    position: absolute; left: 696px; top: 50px;
    font-size: 19px; line-height: 23px; font-weight: 400;
    color: var(--ink-purple);
  }
  .contact { position: absolute; left: 369px; top: 450px; }
  .contact-title { font-size: 17.5px; font-weight: 700; margin-bottom: 16px; }
  .contact-list { list-style: none; }
  .contact-list li {
    display: flex; align-items: center; gap: 9px;
    font-size: 14px; font-weight: 400; height: 24px;
  }
  .contact-icon { width: 16px; height: 16px; flex: none; }
  .tagline {
    position: absolute; left: 696px; top: 458px;
    font-size: 19px; line-height: 23px; font-weight: 400;
  }
  .brand-name {
    position: absolute; left: 806px; top: 662px;
    font-size: 30px; font-weight: 400;
  }
</style>
</head>
<body>
<main class="brochure">
  <svg class="brochure-art" viewBox="0 0 1004 750" width="1004" height="750" aria-hidden="false">
    <defs>
      <linearGradient id="left-panel" x1="0" y1="0" x2="0.3" y2="1">
        <stop offset="0" stop-color="#5a47a0"/>
        <stop offset="0.55" stop-color="#3f6cb3"/>
        <stop offset="1" stop-color="#08b7d6"/>
      </linearGradient>
      <linearGradient id="mid-panel" x1="0" y1="0" x2="0" y2="1">
        <stop offset="0" stop-color="#5548a2"/>
        <stop offset="1" stop-color="#3a62ac"/>
      </linearGradient>
      <linearGradient id="right-panel" x1="0" y1="0" x2="0.4" y2="1">
        <stop offset="0" stop-color="#3e68b1"/>
        <stop offset="1" stop-color="#574aa0"/>
      </linearGradient>
      <linearGradient id="photo-tone" x1="0" y1="0" x2="1" y2="1">
        <stop offset="0" stop-color="#eef1f4"/>
        <stop offset="0.6" stop-color="#c9cfd6"/>
        <stop offset="1" stop-color="#6c7280"/>
      </linearGradient>
      <linearGradient id="portrait-tone" x1="0" y1="0" x2="0" y2="1">
        <stop offset="0" stop-color="#9aa0a8"/>
        <stop offset="1" stop-color="#2c2f36"/>
      </linearGradient>
      <linearGradient id="wave-mid" x1="0" y1="1" x2="1" y2="0">
        <stop offset="0" stop-color="#08b7d6"/>
        <stop offset="1" stop-color="#3a62ac" stop-opacity="0"/>
      </linearGradient>
      <linearGradient id="fold-shade" x1="0" y1="0" x2="1" y2="0">
        <stop offset="0" stop-color="#000" stop-opacity="0"/>
        <stop offset="1" stop-color="#000" stop-opacity="0.14"/>
      </linearGradient>
      <clipPath id="left-clip"><rect x="0" y="0" width="341" height="750"/></clipPath>
    </defs>

    <!-- panels -->
    <rect class="panel-left" x="0" y="0" width="341" height="750" fill="url(#left-panel)"/>
    <rect class="panel-middle" x="341" y="0" width="338" height="750" fill="url(#mid-panel)"/>
    <rect class="panel-right" x="679" y="0" width="325" height="750" fill="url(#right-panel)"/>

    <!-- lower waves -->
    <path class="wave-middle" d="M341 750 L341 690 C420 600 520 570 679 585 L679 750 Z" fill="url(#wave-mid)" opacity="0.9"/>
    <path class="wave-right" d="M679 585 C760 600 830 610 880 580 C930 550 970 520 1004 500 L1004 750 L679 750 Z" fill="#2f8fcb" opacity="0.55"/>

    <!-- portrait -->
    <g clip-path="url(#left-clip)">
      <circle class="portrait-ring" cx="96" cy="156" r="147" fill="#08b4d4"/>
      <circle class="portrait" cx="90" cy="156" r="146" fill="url(#portrait-tone)" role="img" aria-label="Portrait photo of the company founder"/>
    </g>

    <!-- cyan band and photo -->
    <path class="photo-band" d="M344 20 C380 250 520 440 676 448 C820 455 930 400 1004 350 L1004 316 C930 360 820 392 676 392 C516 380 404 204 341 0 Z" fill="#08b4d4"/>
    <path class="photo-band-soft" d="M341 0 C404 204 516 360 676 392 C820 392 930 360 1004 316 L1004 330 C930 372 820 410 676 412 C516 400 400 220 341 10 Z" fill="#1c9fcf" opacity="0.7"/>
    <path class="workspace-photo" d="M341 0 L1004 0 L1004 316 C930 360 820 392 676 392 C516 380 404 204 341 0 Z" fill="url(#photo-tone)" role="img" aria-label="Photo of hands typing on a laptop keyboard"/>

    <!-- folds -->
    <rect x="311" y="0" width="30" height="750" fill="url(#fold-shade)"/>
    <rect x="649" y="0" width="30" height="750" fill="url(#fold-shade)"/>
  </svg>

  <section class="panel-about">
    <p class="profile-name">Marcus Hale, MHA, MBA, CHCIO<br>President and CEO</p>
    <p class="profile-bio">Marcus is the founder and CEO of Brevalink Healthcare Solutions. He has been working in the technology industry for over 25 years with extensive experience in healthcare IT. Marcus has held multiple roles including Chief Information Officer, Chief Information Security Officer, and the executive sponsor of multiple electronic health record (EHR) implementations. He has created and nurtured numerous successful IT departments and built strong relationships with leadership teams. Marcus holds a Master’s in Business Administration and a Master’s in Healthcare Administration, and is certified with the Guild of Healthcare Data Leadership Executives (GHDLE).</p>
  </section>

  <section class="contact">
    <h2 class="contact-title">Contact Us</h2>
    <ul class="contact-list">
      <li>
        <svg class="contact-icon" viewBox="0 0 16 16"><circle cx="8" cy="8" r="8" fill="#fff"/><rect x="4" y="5" width="8" height="6" fill="none" stroke="#4b54a8" stroke-width="1.2"/><path d="M4 5 L8 8.5 L12 5" fill="none" stroke="#4b54a8" stroke-width="1.2"/></svg>
        mhale@brevalinkpro.com
      </li>
      <li>
        <svg class="contact-icon" viewBox="0 0 16 16"><circle cx="8" cy="8" r="8" fill="#fff"/><path d="M4 8 L8 4.5 L12 8 L12 12 L4 12 Z" fill="#4b54a8"/></svg>
        www.brevalinkpro.com
      </li>
      <li>
        <svg class="contact-icon" viewBox="0 0 16 16"><circle cx="8" cy="8" r="8" fill="#fff"/><path d="M5.5 4.5 L7 4.5 L7.6 6.6 L6.6 7.3 C7 8.3 7.7 9 8.7 9.4 L9.4 8.4 L11.5 9 L11.5 10.5 C8 11 5 8 5.5 4.5 Z" fill="#4b54a8"/></svg>
        555-014-2682
      </li>
    </ul>
  </section>

  <h1 class="headline">Increasing the Value<br>and Security of Your<br>Technology Resources</h1>
  <p class="tagline">Providing Information<br>Technology expertise<br>to post-acute care providers</p>
  <p class="brand-name">Your Logo</p>
</main>
</body>
</html>
```